Valmorena.lu - Patrimoine en sérénité

As a rule, most people plan everything meticulously down to the smallest detail, at least when it comes to aspects such as building a house, buying a car, or making major purchases. However, very few think about what is usually the single biggest “transaction” of their entire lives and make provisions for it. We are talking about inheritance – or, from the other perspective, inheriting. In any case, it is about estate planning.

Target Market(s)

Inheritance of a property - People that inheritated a property

Industry/Entity Type

Inheritance of a property - Real Estate

Number of Pages Required

4 page

Font styles to use
Decorative

Colors
0054AA
0677BA
7BADD7
CADEEF
E8F1F8

Requirements
Must have
• Four different Navigation buttons: 1. Immobilier (if somebody inherated a house or flat) 2. Services (if people do not kow what to do) 3. Calculatrice (if people want to get an idea of the value of the house or flat) 4. Contact (to get in touch with us through a text form).
Nice to have
• Since visitors to this site may be in mourning, the website should be very user-friendly and welcoming.
Should not have
• Too bright, too many colors...

```html
<!DOCTYPE html>
<html lang="en">
<head>
<meta charset="utf-8">
<title>Valmorena.lu - Patrimoine en sérénité</title>
<link href="https://fonts.googleapis.com/css2?family=Poppins:wght@400;500;600;700;800&display=swap" rel="stylesheet">
<style>
:root{
  --blue:#0054AA;
  --blue-mid:#0677BA;
  --blue-soft:#7BADD7;
  --blue-pale:#CADEEF;
  --blue-mist:#E8F1F8;
  --ink:#1b1b1f;
  --text:#3b3f48;
  --white:#ffffff;
}
*{margin:0;padding:0;box-sizing:border-box}
html,body{width:1200px;height:5106px;overflow:hidden}
body{font-family:'Poppins',sans-serif;color:var(--text);background:var(--white);position:relative}
.abs{position:absolute}
.accent{color:var(--blue)}
.label{font-size:21px;color:var(--blue-mid);font-weight:400}
.btn{position:absolute;display:flex;align-items:center;justify-content:space-between;background:var(--blue);color:#fff;font-size:11px;font-weight:700;text-transform:uppercase;border-radius:20px;padding:0 4px 0 20px;height:36px}
.btn .arr{width:30px;height:30px;border-radius:50%;background:var(--blue-pale);display:flex;align-items:center;justify-content:center}
.vline{position:absolute;width:2px;background:var(--blue)}
p{line-height:1.6}

/* header */
.header{left:0;top:0;width:1200px;height:84px}
.logo{display:flex;align-items:center;gap:8px;font-weight:700;font-size:20px;color:var(--ink)}
.logo .sq{width:14px;height:14px;border:2px solid var(--blue);border-radius:3px}
.nav{left:312px;top:30px;display:flex;gap:40px;font-size:11px;font-weight:600;color:var(--ink);text-transform:uppercase}
.nav .active{color:var(--blue)}
.call{left:800px;top:24px;width:200px;height:34px;border-radius:18px;background:var(--blue);color:#fff;font-size:10px;font-weight:700;display:flex;align-items:center;justify-content:space-between;padding:0 3px 0 16px}
.call .ic{width:28px;height:28px;border-radius:50%;background:var(--blue-pale);display:flex;align-items:center;justify-content:center}

/* hero */
.hero{left:0;top:0;width:1200px;height:760px;background:linear-gradient(180deg,#eef4fa,#f7fafd 60%,#ffffff)}
.hero h1{font-size:54px;line-height:1.0;font-weight:700;color:var(--ink);letter-spacing:-.5px}
.hero-block{left:852px;top:84px;width:348px;height:676px;background:var(--blue)}
.hero-photo{left:570px;top:158px;width:630px;height:462px;background:linear-gradient(135deg,#6f6457,#a79276 45%,#c9a070 70%,#7a6a5a);border-radius:6px}
.frame{border:2px solid var(--blue);border-radius:6px}
.circ-btn{width:36px;height:36px;border-radius:50%;border:2px solid #fff;display:flex;align-items:center;justify-content:center}

/* immobilier */
.sec-title{font-size:40px;font-weight:700;color:var(--ink);text-align:center}
.feature{width:300px}
.feature .icon{width:76px;height:76px;border-radius:50%;border:3px solid var(--blue);display:flex;align-items:center;justify-content:center}
.feature h3{font-size:17px;font-weight:600;color:var(--ink);margin:38px 0 18px}
.feature p{font-size:13.5px;line-height:1.6}
.feature-card{left:434px;top:1092px;width:332px;height:328px;background:#fff;box-shadow:0 8px 30px rgba(0,40,90,.12)}

/* about */
.about-block{left:0;top:1518px;width:380px;height:704px;background:var(--blue)}
.about-photo{left:0;top:1642px;width:620px;height:460px;border-radius:0 10px 10px 0;background:radial-gradient(circle at 50% 55%,#d9373a 0 10%,#c99272 22%,#8aa4b8 60%,#5c7e97)}
.badge{left:570px;top:1876px;width:100px;height:100px;border-radius:50%;background:var(--blue);border:4px solid #fff;box-shadow:0 0 0 2px var(--blue);color:#fff;display:flex;align-items:center;justify-content:center;font-weight:700;font-size:26px}
.h2{font-size:43px;line-height:1.05;font-weight:700;color:var(--ink);letter-spacing:-.3px}

/* services */
.services{left:0;top:2222px;width:1200px;height:950px;background:var(--blue-mist)}
.svc{width:454px;height:232px;background:#fff;box-shadow:0 6px 24px rgba(0,40,90,.08);padding:46px 30px 0 142px}
.svc .icon{position:absolute;left:32px;top:50px;width:78px;height:78px;border-radius:50%;border:2px solid var(--blue);display:flex;align-items:center;justify-content:center}
.svc h3{font-size:17px;font-weight:600;color:var(--ink);margin-bottom:10px}
.svc p{font-size:13.5px;line-height:1.6}

/* calculator */
.calc{left:0;top:3172px;width:1200px;height:530px;background:linear-gradient(180deg,#06306e,#0a4ba0 45%,#0f54ad)}
.calc-img{left:0;top:0;width:660px;height:530px;clip-path:polygon(0 0,58% 0,100% 30%,70% 100%,0 100%);background:linear-gradient(160deg,#1d3b73,#35527e 40%,#9a8a77 70%,#2a4e8e)}
.calc h2{font-size:37px;line-height:1.1;font-weight:700;color:#fff}

/* contact */
.contact{left:0;top:3702px;width:1200px;height:870px;background:linear-gradient(180deg,#eef4fa,#dde9f5)}
.form{left:222px;top:3966px;width:756px;height:494px;background:var(--blue-mid);background:linear-gradient(160deg,#0c5fb6,#0054AA);border-radius:24px}
.field{position:absolute;background:#fff;border:1px solid var(--blue-pale);font-size:12.5px;color:#555;padding:14px 18px}

/* footer */
.foot-item{width:240px;text-align:center;font-size:12px;color:var(--ink)}
.foot-item .ic{width:52px;height:52px;border-radius:50%;background:var(--blue);margin:0 auto 14px;display:flex;align-items:center;justify-content:center}
.foot-h{font-size:13px;font-weight:700;color:var(--ink);text-transform:uppercase}
.social{width:30px;height:30px;border-radius:50%;background:var(--ink)}
</style>
</head>
<body>

<!-- HERO -->
<section class="abs hero"></section>
<div class="abs hero-block"></div>
<div class="abs frame" style="left:542px;top:392px;width:246px;height:256px"></div>
<div class="abs hero-photo" role="img" aria-label="Elderly man signing an inheritance document at a wooden desk"></div>
<div class="abs" style="left:858px;top:358px;width:64px;height:64px;border-radius:50%;background:rgba(30,30,30,.55);display:flex;align-items:center;justify-content:center">
  <svg width="20" height="22" viewBox="0 0 20 22"><path d="M3 2l15 9-15 9z" fill="#fff"/></svg>
</div>
<div class="abs circ-btn" style="left:987px;top:648px"><svg width="16" height="12" viewBox="0 0 16 12"><path d="M15 6H2M6 1L1 6l5 5" stroke="#fff" stroke-width="1.8" fill="none"/></svg></div>
<div class="abs circ-btn" style="left:1033px;top:648px"><svg width="16" height="12" viewBox="0 0 16 12"><path d="M1 6h13M10 1l5 5-5 5" stroke="#fff" stroke-width="1.8" fill="none"/></svg></div>

<header class="abs header">
  <div class="abs logo" style="left:128px;top:28px"><span class="sq"></span>Valmorena.lu</div>
  <nav class="abs nav">
    <span class="active">Home</span><span>Immobilier</span><span>Services</span><span>Calculatrice</span><span>Contact</span>
  </nav>
  <div class="abs" style="left:312px;top:82px;width:36px;height:2px;background:var(--blue)"></div>
  <div class="abs call">CALL +1 (555) 0142-7730<span class="ic"><svg width="14" height="14" viewBox="0 0 24 24"><path d="M6.6 10.8a15 15 0 006.6 6.6l2.2-2.2c.3-.3.7-.4 1-.2 1.1.4 2.3.6 3.6.6.6 0 1 .4 1 1V20c0 .6-.4 1-1 1A17 17 0 013 4c0-.6.4-1 1-1h3.5c.6 0 1 .4 1 1 0 1.3.2 2.5.6 3.6.1.3 0 .7-.2 1z" fill="var(--blue)"/></svg></span></div>
  <div class="abs" style="left:1020px;top:34px;font-size:11px;font-weight:700;color:var(--ink)">ENG &nbsp;⌄</div>
</header>

<div class="abs" style="left:128px;top:206px;font-size:19px;color:var(--blue-mid)">Valmorena.lu</div>
<div class="abs hero" style="background:none;left:128px;top:246px;width:420px;height:auto">
  <h1>Inheritance made <span class="accent">simple,</span> <span class="accent">secure,</span> and respectful.</h1>
</div>
<p class="abs" style="left:130px;top:478px;width:320px;font-size:13.5px;color:var(--ink)">We help you handle inherited property with clarity, professionalism, and care.</p>
<div class="btn" style="left:130px;top:548px;width:196px">Request valuation<span class="arr"><svg width="12" height="12" viewBox="0 0 12 12"><path d="M2 10L10 2M4 2h6v6" stroke="var(--blue)" stroke-width="1.6" fill="none"/></svg></span></div>
<div class="vline" style="left:599px;top:728px;height:78px"></div>

<!-- IMMOBILIER -->
<div class="abs label" style="left:0;top:838px;width:1200px;text-align:center">Immobilier</div>
<h2 class="abs sec-title" style="left:0;top:872px;width:1200px">Inherited <span class="accent">Real Estate</span></h2>
<p class="abs" style="left:185px;top:944px;width:830px;text-align:center;font-size:13.5px">Lorem ipsum dolor sit amet, consectetur adipiscing elit, sed do eiusmod tempor incididunt ut labore et dolore magna aliqua. Ut enim ad minim veniam, quis nostrud exercitation ullamco laboris nisi ut aliquip ex ea commodo consequat. Duis aute irure dolor in reprehenderit in voluptate velit esse cillum dolore eu fugiat nulla pariatur. Excepteur sint occaecat cupidatat non proident, sunt in culpa qui officia deserunt mollit anim id est laborum.</p>

<div class="abs feature-card"></div>
<div class="abs" style="left:500px;top:1418px;width:196px;height:3px;background:var(--blue)"></div>
<div class="abs feature" style="left:130px;top:1126px">
  <div class="icon"><svg width="34" height="34" viewBox="0 0 24 24"><path d="M4 12.5l5 5L20 6.5" stroke="var(--blue)" stroke-width="3" fill="none" stroke-linecap="round"/></svg></div>
  <h3>Evaluate</h3>
  <p>Lorem ipsum dolor sit amet, consectetur adipiscing elit, sed do eiusmod tempor incididunt ut labore et dolore magna aliqua. Ut enim ad minim veniam, quis</p>
</div>
<div class="abs feature" style="left:485px;top:1126px">
  <div class="icon"><svg width="36" height="36" viewBox="0 0 24 24"><circle cx="12" cy="12" r="10" fill="var(--blue)"/><path d="M12 6v6l4 2" stroke="#fff" stroke-width="2" fill="none"/></svg></div>
  <h3>Manage</h3>
  <p>Lorem ipsum dolor sit amet, consectetur adipiscing elit, sed do eiusmod tempor incididunt ut labore et dolore magna aliqua. Ut enim ad minim veniam, quis</p>
</div>
<div class="abs feature" style="left:838px;top:1126px">
  <div class="icon"><svg width="38" height="36" viewBox="0 0 24 22"><path d="M12 2L1 11h3v9h6v-6h4v6h6v-9h3z" fill="var(--blue)"/></svg></div>
  <h3>Sell</h3>
  <p>Lorem ipsum dolor sit amet, consectetur adipiscing elit, sed do eiusmod tempor incididunt ut labore et dolore magna aliqua. Ut enim ad minim veniam, quis</p>
</div>

<!-- ABOUT -->
<div class="abs about-block"></div>
<div class="abs frame" style="left:560px;top:1860px;width:76px;height:262px;border-left:none;border-radius:0 10px 10px 0"></div>
<div class="abs about-photo" role="img" aria-label="Two cupped hands holding a small red house figure"></div>
<div class="abs badge">25+</div>
<div class="abs label" style="left:706px;top:1652px">About Valmorena.lu</div>
<h2 class="abs h2" style="left:704px;top:1688px;width:420px">Inheritance made <span class="accent">simple, secure,</span> and respectful.</h2>
<p class="abs" style="left:706px;top:1838px;width:370px;font-size:13px;color:var(--ink)">Real Estate Estate: What is this important value? Every year, some people in Luxembourg find themselves in the situation of real estate estate inheritance. They gather on this site the essential points that allow them to safely and securely handle all administrative procedures.<br>Below are some tips on how to complete real estate assets (inheritance) and how to understand ownership issues. We preserve the values.</p>
<div class="btn" style="left:706px;top:2058px;width:154px">Learn more<span class="arr"><svg width="12" height="12" viewBox="0 0 12 12"><path d="M2 10L10 2M4 2h6v6" stroke="var(--blue)" stroke-width="1.6" fill="none"/></svg></span></div>

<!-- SERVICES -->
<section class="abs services"></section>
<div class="vline" style="left:597px;top:2192px;height:74px"></div>
<div class="abs label" style="left:128px;top:2348px">Our Services</div>
<h2 class="abs h2" style="left:128px;top:2384px;font-size:42px;line-height:1.28">Guidance in<br>Difficult <span class="accent">Times</span></h2>
<p class="abs" style="left:628px;top:2346px;width:446px;font-size:13.5px;line-height:1.75">Lorem ipsum dolor sit amet, consectetur adipiscing elit, sed do eiusmod tempor incididunt ut labore et dolore magna aliqua. Ut enim ad minim veniam, quis nostrud exercitation ullamco laboris nisi ut aliquip ex ea commodo consequat. Duis aute irure dolor in reprehenderit in voluptate velit esse cillum dolore eu fugiat nulla pariatur.</p>

<div class="abs svc" style="left:130px;top:2558px">
  <div class="icon"><svg width="36" height="36" viewBox="0 0 24 24" fill="none" stroke="var(--blue)" stroke-width="1.4"><path d="M6 2h9l4 4v16H6z"/><path d="M9 9h7M9 12h7M9 15h5"/></svg></div>
  <h3>Legal support &amp; documentation</h3>
  <p>Lorem ipsum dolor sit amet, consectetur adipiscing elit, sed do eiusmod tempor incididunt ut labore et dolore magna aliqua. Ut enim ad minim veniam, quis nostrud</p>
</div>
<div class="abs svc" style="left:614px;top:2558px">
  <div class="icon"><svg width="36" height="36" viewBox="0 0 24 24" fill="none" stroke="var(--blue)" stroke-width="1.4"><path d="M4 22V8h8v14M12 22V3h8v19M2 22h20"/><path d="M7 11h2M7 14h2M7 17h2M15 7h2M15 10h2M15 13h2M15 16h2"/></svg></div>
  <h3>Property management</h3>
  <p>Lorem ipsum dolor sit amet, consectetur adipiscing elit, sed do eiusmod tempor incididunt ut labore et dolore magna aliqua. Ut enim ad minim veniam, quis nostrud</p>
</div>
<div class="abs svc" style="left:130px;top:2818px">
  <div class="icon"><svg width="36" height="36" viewBox="0 0 24 24" fill="none" stroke="var(--blue)" stroke-width="1.4"><path d="M2 11L12 3l10 8M5 9v12h14V9"/><rect x="8" y="13" width="8" height="5"/></svg></div>
  <h3>Sale of inherited property</h3>
  <p>Lorem ipsum dolor sit amet, consectetur adipiscing elit, sed do eiusmod tempor incididunt ut labore et dolore magna aliqua. Ut enim ad minim veniam, quis nostrud</p>
</div>
<div class="abs svc" style="left:614px;top:2818px">
  <div class="icon"><svg width="36" height="36" viewBox="0 0 24 24" fill="none" stroke="var(--blue)" stroke-width="1.4"><circle cx="7" cy="6" r="2.5"/><circle cx="17" cy="6" r="2.5"/><path d="M3 21v-8c0-2 2-3 4-3s4 1 4 3v8M13 21v-8c0-2 2-3 4-3s4 1 4 3v8"/></svg></div>
  <h3>Advice &amp; consultation</h3>
  <p>Lorem ipsum dolor sit amet, consectetur adipiscing elit, sed do eiusmod tempor incididunt ut labore et dolore magna aliqua. Ut enim ad minim veniam, quis nostrud</p>
</div>

<!-- CALCULATOR -->
<section class="abs calc">
  <div class="abs calc-img" role="img" aria-label="Hand holding a small lit house model over a blue field at dusk"></div>
  <div class="abs" style="left:704px;top:102px;font-size:21px;color:var(--blue-pale)">Calculatrice</div>
  <h2 class="abs" style="left:704px;top:134px;width:420px">Inheritance Property Calculator</h2>
  <p class="abs" style="left:704px;top:236px;width:366px;font-size:13px;color:#fff">Lorem ipsum dolor sit amet, consectetur adipiscing elit, sed do eiusmod tempor incididunt ut labore et dolore magna aliqua. Ut enim ad minim veniam, quis nostrud exercitation</p>
  <div class="btn" style="left:706px;top:352px;width:194px;background:var(--blue-mid)">Request valuation<span class="arr"><svg width="12" height="12" viewBox="0 0 12 12"><path d="M2 10L10 2M4 2h6v6" stroke="var(--blue)" stroke-width="1.6" fill="none"/></svg></span></div>
</section>

<!-- CONTACT -->
<section class="abs contact"></section>
<div class="abs label" style="left:0;top:3782px;width:1200px;text-align:center">Contact Us</div>
<h2 class="abs sec-title" style="left:0;top:3816px;width:1200px;font-size:42px;line-height:1.25">Let’s Talk About Your<br><span style="color:var(--blue-mid)">Inheritance</span> Needs</h2>
<div class="abs form">
  <div class="field" style="left:62px;top:74px;width:308px;height:44px">First name</div>
  <div class="field" style="left:384px;top:74px;width:310px;height:44px">Last name</div>
  <div class="field" style="left:62px;top:134px;width:308px;height:44px">Email address</div>
  <div class="field" style="left:384px;top:134px;width:310px;height:44px">Phone</div>
  <div class="field" style="left:62px;top:196px;width:632px;height:168px">Message</div>
  <div class="btn" style="left:318px;top:410px;width:120px;background:#0a3f88">Submit<span class="arr"><svg width="12" height="12" viewBox="0 0 12 12"><path d="M2 10L10 2M4 2h6v6" stroke="var(--blue)" stroke-width="1.6" fill="none"/></svg></span></div>
</div>

<!-- FOOTER -->
<svg class="abs" style="left:556px;top:4538px" width="88" height="34" viewBox="0 0 88 34"><path d="M0 34L44 0l44 34z" fill="#fff"/></svg>
<div class="abs" style="left:589px;top:4562px;width:22px;height:22px;border-radius:50%;background:var(--blue);color:#fff;font-size:11px;font-weight:700;text-align:center;line-height:22px">↓</div>
<div class="abs foot-item" style="left:182px;top:4650px">
  <div class="ic"><svg width="18" height="22" viewBox="0 0 24 30"><path d="M12 1a10 10 0 00-10 10c0 8 10 18 10 18s10-10 10-18A10 10 0 0012 1z" fill="#fff"/><circle cx="12" cy="11" r="3.5" fill="var(--blue)"/></svg></div>
  120 Nemo enim ipsam<br>voluptatem quia voluptas
</div>
<div class="abs" style="left:444px;top:4654px;width:1px;height:84px;background:var(--blue-pale)"></div>
<div class="abs foot-item" style="left:470px;top:4650px">
  <div class="ic"><svg width="20" height="20" viewBox="0 0 24 24"><path d="M6.6 10.8a15 15 0 006.6 6.6l2.2-2.2c.3-.3.7-.4 1-.2 1.1.4 2.3.6 3.6.6.6 0 1 .4 1 1V20c0 .6-.4 1-1 1A17 17 0 013 4c0-.6.4-1 1-1h3.5c.6 0 1 .4 1 1 0 1.3.2 2.5.6 3.6.1.3 0 .7-.2 1z" fill="#fff"/></svg></div>
  Call<br><b style="font-weight:600">+1 (555) 0142-7730</b>
</div>
<div class="abs" style="left:722px;top:4654px;width:1px;height:84px;background:var(--blue-pale)"></div>
<div class="abs foot-item" style="left:758px;top:4650px">
  <div class="ic"><svg width="22" height="16" viewBox="0 0 22 16"><rect x="1" y="1" width="20" height="14" rx="2" fill="#fff"/><path d="M1 2l10 7 10-7" stroke="var(--blue)" stroke-width="1.6" fill="none"/></svg></div>
  Email<br>info@valmorena.lu
</div>

<div class="abs logo" style="left:128px;top:4852px"><span class="sq"></span>Valmorena.lu</div>
<div class="abs" style="left:128px;top:4906px;display:flex;gap:8px">
  <span class="social"></span><span class="social"></span><span class="social"></span><span class="social"></span><span class="social"></span>
</div>
<div class="abs foot-h" style="left:452px;top:4836px">Quick Links</div>
<div class="abs" style="left:452px;top:4872px;font-size:12px;line-height:2.1;color:var(--ink)">Immobilier<br>Services</div>
<div class="abs" style="left:576px;top:4872px;font-size:12px;line-height:2.1;color:var(--ink)">Calculatrice<br>Contact</div>
<div class="abs foot-h" style="left:816px;top:4836px">Subscribe to our newsletter</div>
<div class="abs" style="left:816px;top:4884px;font-size:10px;color:var(--ink)">Email Address:</div>
<div class="abs" style="left:1036px;top:4876px;width:30px;height:30px;border-radius:50%;background:var(--blue);display:flex;align-items:center;justify-content:center"><svg width="12" height="12" viewBox="0 0 12 12"><path d="M2 10L10 2M4 2h6v6" stroke="#fff" stroke-width="1.6" fill="none"/></svg></div>
<div class="abs" style="left:816px;top:4924px;width:252px;height:1px;background:var(--blue-pale)"></div>
<div class="abs" style="left:130px;top:4996px;width:940px;height:1px;background:#e3e8ee"></div>
<div class="abs" style="left:0;top:5042px;width:1200px;text-align:center;font-size:12px;color:var(--ink)">© Copyright 2025 Valmorena.lu. All rights reserved</div>

</body>
</html>
```